Doctors Office Web Design

Name of the business is Lin-Yue Hart M.D.
We need a web design that is attractive for women that want to see Dr. Lin-Yue Hart for Obstetrician Gynecology and Pregnancy care. Dr. Hart earned her degree from Carrow Ridge Medical College of obstetrician gynecology. We want to attract women of child bearing ages to come to our offices for health, education, and pregnancies.

Please visit http://www.drhartclinicweb.com/ to help you get a feel for who we are. We will be adding some pictures and logo in the next few days.

We are looking for to have pages for and tabs including
About Us- History, Our Staff, Dr. Hart
Patient Information- Appointments, E-Prescriptions, Payments Accepted, Insurance
Health- General, Sexual, Mental, Affiliates
Pregnancy- Minimally invasive surgery(our specialty), 4-D Ultra Sound, Hospital Affiliations
Media- News,Pictures, Videos
Locations- Palmer Office, Westvale Office

The colors we would like to use are pastel colors, magenta, and plum

Target Market(s)

Women of all ages with an emphasis on 25-65 year olds

Industry/Entity Type

Business

Requirements
Must have
• Needs to include a location for a our videos and pictures that I will submit shortly. We also want a map to our location or atleast a place for one.
Nice to have
• A place for a google map of our office locations.

```html
<!DOCTYPE html>
<html lang="en">
<head>
<meta charset="utf-8">
<title>Lin-Yue Hart M.D.</title>
<link rel="stylesheet" href="https://fonts.googleapis.com/css2?family=Noto+Sans:wght@400;700&display=swap">
<style>
  :root{
    --sky-top:#f3d3ea;
    --sky-bottom:#d9a6cf;
    --nav-top:#b0589e;
    --nav-bottom:#7a2f72;
    --page:#f4eff3;
    --panel:#ffffff;
    --accent:#b2388f;
    --button:#b8489c;
    --menu-top:#e39bd0;
    --menu-bottom:#a4408f;
    --text:#555555;
    --footer:#9a5a94;
    --footer-dark:#83467f;
    --white:#ffffff;
  }
  *{box-sizing:border-box;margin:0;padding:0}
  html,body{width:810px;height:1200px;overflow:hidden}
  body{position:relative;background:var(--page);font-family:"Noto Sans",Verdana,sans-serif;color:var(--text)}
  a{color:inherit;text-decoration:none}
  .abs{position:absolute}

  .site-header{position:absolute;left:0;top:0;width:810px;height:160px;background:linear-gradient(var(--sky-top),var(--sky-bottom));border-bottom:1px solid #c98fbd}
  .brand{left:46px;top:44px;display:flex;align-items:center;gap:8px;color:var(--white);font-size:23px;letter-spacing:.5px}
  .brand-dot{width:10px;height:10px;border-radius:50%;background:var(--white)}
  .account{right:46px;top:32px;font-size:12px;color:var(--white);text-decoration:underline}
  .search{left:477px;top:59px;width:189px;height:23px;background:var(--white);border-radius:3px}
  .search svg{position:absolute;left:8px;top:4px}
  .search-btn{left:674px;top:59px;width:90px;height:23px;background:linear-gradient(#f6f6f6,#d5d5d5);border:1px solid #b9b9b9;border-radius:3px;font-size:12px;color:#111;text-align:center;line-height:21px}

  .main-nav{left:44px;top:120px;width:721px;height:40px;background:linear-gradient(var(--nav-top),var(--nav-bottom));border-radius:4px 4px 0 0;display:flex}
  .main-nav a{flex:1;color:var(--white);font-size:15px;text-align:center;line-height:40px;border-right:1px solid rgba(255,255,255,.25);white-space:nowrap}
  .main-nav a:last-child{border-right:none}

  .hero-photo{left:44px;top:160px;width:378px;height:238px;background:linear-gradient(135deg,#f7f3f6,#efe2ec 50%,#e2cadc)}
  .hero-copy{left:430px;top:204px;width:328px;text-align:center;color:var(--accent);font-size:20px;line-height:23px}
  .hero-copy p+p{margin-top:30px}

  .side-menu{left:44px;top:417px;width:237px;height:129px;background:linear-gradient(var(--menu-top),var(--menu-bottom));border:1px solid #a4408f;border-radius:3px;padding:5px 0 0 9px;list-style:none}
  .side-menu li{color:var(--white);font-size:19px;line-height:27px;padding-left:18px;position:relative;margin-bottom:5px}
  .side-menu li::before{content:"";position:absolute;left:1px;top:11px;width:9px;height:9px;border-radius:50%;background:var(--white)}
  .side-menu li:not(:last-child)::after{content:"";position:absolute;left:38px;right:48px;bottom:-3px;height:1px;background:rgba(255,255,255,.6)}

  .panel{background:var(--panel)}
  .intro{left:309px;top:417px;width:456px;height:129px}
  .body-copy{font-size:11px;line-height:16px;color:var(--text);white-space:nowrap}
  .intro .body-copy{position:absolute;left:17px;top:20px}
  .more{position:absolute;background:var(--button);color:var(--white);font-size:11px;text-align:center;line-height:18px}

  .feature{left:44px;top:560px;width:721px;height:190px;background:linear-gradient(90deg,#fff,#f8f6f8)}
  .feature-photo{position:absolute;left:2px;top:2px;width:234px;height:188px;background:linear-gradient(120deg,#f4f2f3,#ecdcd4 55%,#d3ad98)}
  .feature .body-copy{position:absolute;left:272px;top:11px}

  .media{left:44px;top:760px;width:721px;height:212px}
  .news{position:absolute;left:9px;top:10px;width:166px;height:191px;background:#f3eef2}
  .news-title{height:21px;background:var(--button);color:var(--white);font-size:11.5px;text-align:center;line-height:21px}
  .news p{font-size:11px;line-height:16px;text-align:justify;padding:2px 2px 0 4px}
  .gallery{position:absolute;left:182px;top:11px;width:232px;height:190px;background:linear-gradient(160deg,#e8e0e6,#f7f4f6 45%,#dcbcaa 75%,#f1eef0)}
  .gallery-label{position:absolute;left:67px;top:87px;width:104px;height:25px;background:var(--button);color:var(--white);font-size:12px;text-align:center;line-height:25px}
  .video{position:absolute;left:430px;top:2px;width:288px;height:169px;border-radius:5px;background:linear-gradient(#3b3b3b,#111 60%,#000);border:1px solid #555}
  .video-caption{position:absolute;left:0;width:100%;top:136px;text-align:center;color:var(--white);font-size:12px}
  .player{position:absolute;left:430px;top:176px;width:288px;height:35px;border-radius:4px;background:linear-gradient(#5a5a5a,#1e1e1e);border:1px solid #666}

  .site-footer{left:0;top:1000px;width:810px;height:156px;background:var(--footer);border-top:2px solid #874a82}
  .footer-list{position:absolute;list-style:none}
  .footer-list li{color:var(--white);font-size:12px;height:27px;padding-left:22px;position:relative}
  .footer-list li::before{content:"";position:absolute;left:0;top:6px;width:6px;height:6px;border-radius:50%;background:var(--white)}
  .footer-links{position:absolute;top:120px;color:var(--white);font-size:12px}
  .legal{left:0;top:1156px;width:810px;height:44px;background:var(--footer-dark);border-top:3px solid #f1dcec;color:var(--white);font-size:12px;text-align:center;line-height:56px}
</style>
</head>
<body>
  <header class="site-header">
    <div class="abs brand"><span class="brand-dot"></span>Lin-Yue Hart M.D.</div>
    <a class="abs account" href="#">Log in | Register</a>
    <div class="abs search">
      <svg width="22" height="16" viewBox="0 0 22 16"><circle cx="7" cy="6" r="5" fill="none" stroke="#bbb" stroke-width="2"/><line x1="11" y1="10" x2="17" y2="15" stroke="#bbb" stroke-width="3" stroke-linecap="round"/></svg>
    </div>
    <div class="abs search-btn">Search</div>
  </header>

  <nav class="abs main-nav">
    <a href="#">Home</a><a href="#">About Us</a><a href="#">Our Staff</a><a href="#">Dr. Hart</a><a href="#">Health</a><a href="#">Pregnancy</a><a href="#">Media</a><a href="#">Locations</a>
  </nav>

  <div class="abs hero-photo" role="img" aria-label="Photo of four smiling doctors in white coats with stethoscopes"></div>
  <div class="abs hero-copy">
    <p>Pregnancy - Mininally inpresive<br>surgery our speciality</p>
    <p>4-D ultra Sound<br>Surgury Cour Speciality</p>
  </div>

  <ul class="abs side-menu">
    <li>Patients Information</li>
    <li>Appointments</li>
    <li>E- Prescription</li>
    <li>Payment</li>
  </ul>

  <section class="abs panel intro">
    <p class="body-copy">Lorem Emsum otherwise permitted by theLinkSession, Remote As-<br>sistance, and Remote Screenpeatures described below, you may not<br>use the Producto permit any Device to use, access, display or run<br>othxecutable software residing on the Workstation Computer,<br>nor may you permit any Device to use, access, display,<br>or run the Product or Product's user interface, unless</p>
    <a class="more" href="#" style="left:389px;top:97px;width:67px">More</a>
  </section>

  <section class="abs feature">
    <div class="feature-photo" role="img" aria-label="Photo of a doctor holding a baby"></div>
    <p class="body-copy">Except as otherwise permitted by the LinkSession, Remote Aid, and<br>Remote Screen features described below, you may not use the Product<br>to permit any Device to use, access, display or run otherexecutable software<br>residing on the Workstation Computer, nor may you permit any Device toac-<br>cess, display, or run the Product or Product's user interface, unless<br>the Device has a separate license for the Product. Except as otherwise mitted<br>by theLinkSession, Remote Aid, and Remote Screen<br>features cense for the Product.</p>
    <a class="more" href="#" style="left:653px;top:160px;width:67px">More</a>
  </section>

  <section class="abs panel media">
    <div class="news">
      <div class="news-title">News Event</div>
      <p>Except as otherwise peuct to permit any Device to use, access, display or run other xecutable software residing on the Workstation Couter,or may you permit any Device <span style="letter-spacing:1.5px">tuse,access,display,</span> oun the Product or Product's <span style="letter-spacing:2px">userinterface,unless</span></p>
      <a class="more" href="#" style="left:101px;top:171px;width:64px;height:17px;font-size:10px;line-height:17px;font-family:Georgia,serif">More</a>
    </div>
    <div class="gallery" role="img" aria-label="Photo of a doctor holding a newborn's hand">
      <div class="gallery-label">Gallery</div>
    </div>
    <div class="video">
      <svg class="abs" style="left:97px;top:47px" width="112" height="80" viewBox="0 0 112 80">
        <circle cx="40" cy="40" r="36" fill="none" stroke="#fff" stroke-width="5"/>
        <circle cx="40" cy="20" r="10" fill="#fff"/><circle cx="40" cy="60" r="10" fill="#fff"/>
        <circle cx="20" cy="40" r="10" fill="#fff"/><circle cx="60" cy="40" r="10" fill="#fff"/>
        <circle cx="40" cy="40" r="4" fill="none" stroke="#fff" stroke-width="2"/>
        <path d="M68 62 Q80 80 106 78" fill="none" stroke="#fff" stroke-width="3"/>
      </svg>
      <div class="video-caption">Click Here For Play Video</div>
    </div>
    <div class="player">
      <svg class="abs" style="left:18px;top:10px" width="32" height="16" viewBox="0 0 32 16"><path d="M0 0 L14 8 L0 16Z" fill="#fff"/><rect x="18" y="1" width="4" height="15" fill="#fff"/><rect x="25" y="1" width="4" height="15" fill="#fff"/></svg>
      <div class="abs" style="left:63px;top:16px;width:200px;height:4px;background:#fff"></div>
      <div class="abs" style="left:82px;top:13px;width:12px;height:9px;background:#c8388f;border:1px solid #fff;border-radius:2px"></div>
    </div>
  </section>

  <footer class="abs site-footer">
    <ul class="footer-list" style="left:56px;top:18px"><li>Maps</li><li>Picture Gallery</li><li>Video Gallery</li></ul>
    <ul class="footer-list" style="left:318px;top:20px"><li>Online Prescription</li><li>Online Payment</li><li>Appoinments</li></ul>
    <ul class="footer-list" style="left:589px;top:19px"><li>Booking</li><li>Your Quary</li></ul>
    <div class="footer-links" style="left:54px">Home | About Us | Dr.Hart</div>
    <div class="footer-links" style="right:49px;top:117px">Log in | Register</div>
  </footer>
  <div class="abs legal">All Right reserved copy right Hart women's care 2011</div>
</body>
</html>
```